Modern, Sleek & Vibrant design required for electrical contracting work.

I require a flyer design for BRANDEL VOLT SERVICES, which operates as an electrical contractor. We do electrical installations such as LED lighting, maintenance, repairs, communications and various other work related for residential and commercial customers. I would like the same colours applied from my logo to the flyer (Electric Blue, White, Grey/Silver). A6 or DL sizes with single side.

Target Market(s)

Residential and Commercial customers.

Industry/Entity Type

Communications

Font styles to use
Serif
Sans Serif

Requirements
Must have
• My logo and colours (Electric Blue, White, Silver/Grey)
Nice to have
• Shapes separating different parts of the flyer, such as the same electric bolt from my logo. Straight or angled shapes.
Should not have
• Childish pictures such as light bulbs. Curved shapes.

```html
<!DOCTYPE html>
<html lang="en">
<head>
<meta charset="utf-8">
<title>Brandel Volt Services – Flyer</title>
<link rel="stylesheet" href="https://fonts.googleapis.com/css2?family=Open+Sans:wght@300;400;600;700&family=Roboto+Condensed:wght@300;400&display=swap">
<style>
  :root {
    --electric-blue: #3a53a4;
    --white: #ffffff;
    --silver: #c4c4c6;
    --silver-light: #f2f2f2;
  }
  html, body {
    margin: 0;
    padding: 0;
    width: 851px;
    height: 1200px;
    overflow: hidden;
    background: var(--white);
  }
  .flyer {
    position: relative;
    width: 851px;
    height: 1200px;
    overflow: hidden;
    background: var(--electric-blue);
    font-family: "Open Sans", Arial, sans-serif;
    color: var(--white);
  }
  .flyer__backdrop {
    position: absolute;
    inset: 0;
  }
  .flyer__title {
    position: absolute;
    left: 37px;
    top: 66px;
    margin: 0;
    font-weight: 600;
    font-size: 49px;
    letter-spacing: 0.5px;
    line-height: 1;
    white-space: nowrap;
  }
  .flyer__rule {
    position: absolute;
    left: 37px;
    top: 142px;
    width: 763px;
    height: 0;
    border-top: 1.5px solid var(--white);
  }
  .services {
    position: absolute;
    left: 37px;
    top: 203px;
    margin: 0;
    padding: 0;
    list-style: none;
  }
  .services__item {
    display: flex;
    align-items: center;
    height: 66.5px;
    font-weight: 300;
    font-size: 49px;
    white-space: nowrap;
  }
  .services__marker {
    width: 26px;
    height: 26px;
    border: 3px solid var(--white);
    border-radius: 50%;
    margin-right: 29px;
    flex: none;
  }
  .contact {
    position: absolute;
    left: 37px;
    top: 700px;
  }
  .contact__role {
    margin: 0;
    font-weight: 700;
    font-size: 23px;
    line-height: 1.2;
    width: 275px;
    padding-bottom: 10px;
    border-bottom: 1.5px solid var(--white);
  }
  .contact__name {
    margin: 6px 0 0;
    font-weight: 400;
    font-size: 25px;
  }
  .contact__details {
    margin: 22px 0 0;
    font-weight: 400;
    font-size: 18px;
    line-height: 1.8;
  }
  .quote-badge {
    position: absolute;
    left: 604px;
    top: 744px;
    width: 186px;
    height: 186px;
    border-radius: 50%;
    background: var(--white);
    border: 5px solid var(--electric-blue);
    box-sizing: border-box;
    box-shadow: 0 0 0 6px var(--white), 0 0 0 11px var(--electric-blue);
    display: flex;
    flex-direction: column;
    align-items: center;
    justify-content: center;
    font-family: "Roboto Condensed", "Arial Narrow", sans-serif;
    font-weight: 300;
    color: var(--electric-blue);
    text-align: center;
    line-height: 0.95;
  }
  .quote-badge__top { font-size: 38px; }
  .quote-badge__main { font-size: 52px; }
  .quote-badge__bottom { font-size: 32px; }
  .brand {
    position: absolute;
    left: 300px;
    top: 1040px;
    display: flex;
    align-items: center;
    color: var(--electric-blue);
    font-weight: 700;
  }
  .brand__dot {
    width: 100px;
    height: 100px;
    border-radius: 50%;
    border: 10px solid var(--electric-blue);
    box-sizing: border-box;
    margin-right: 18px;
    flex: none;
  }
  .brand__name {
    display: flex;
    flex-direction: column;
    line-height: 1;
  }
  .brand__main { font-size: 74px; letter-spacing: 1px; }
  .brand__sub { font-size: 30px; letter-spacing: 2px; margin-top: 4px; }
</style>
</head>
<body>
  <main class="flyer">
    <svg class="flyer__backdrop" width="851" height="1200" viewBox="0 0 851 1200" aria-hidden="true">
      <defs>
        <linearGradient id="silver-sweep" x1="0" y1="0" x2="0" y2="1">
          <stop offset="0" stop-color="var(--silver)" style="stop-color:#c4c4c6"/>
          <stop offset="0.45" stop-color="#e6e6e7"/>
          <stop offset="0.75" stop-color="#ffffff"/>
        </linearGradient>
      </defs>
      <polygon points="851,300 570,455 790,578 355,800 570,885 0,1188 0,1200 851,1200" fill="url(#silver-sweep)"/>
    </svg>

    <h1 class="flyer__title">BRANDEL VOLT SERVICES</h1>
    <div class="flyer__rule"></div>

    <ul class="services">
      <li class="services__item"><span class="services__marker"></span>LED Lighting</li>
      <li class="services__item"><span class="services__marker"></span>Installations</li>
      <li class="services__item"><span class="services__marker"></span>Maintenance</li>
      <li class="services__item"><span class="services__marker"></span>Repairs</li>
      <li class="services__item"><span class="services__marker"></span>Communications</li>
      <li class="services__item"><span class="services__marker"></span>Emergency Call-Outs</li>
    </ul>

    <section class="contact">
      <h2 class="contact__role">DIRECTOR</h2>
      <p class="contact__name">Dario Brandel</p>
      <p class="contact__details">EC Number – EC20463<br>dario@brandelvolt.com</p>
    </section>

    <div class="quote-badge">
      <span class="quote-badge__top">GET A</span>
      <span class="quote-badge__main">FREE</span>
      <span class="quote-badge__bottom">QUOTE</span>
    </div>

    <div class="brand">
      <span class="brand__dot"></span>
      <span class="brand__name">
        <span class="brand__main">BRANDEL</span>
        <span class="brand__sub">VOLT SERVICES</span>
      </span>
    </div>
  </main>
</body>
</html>
```